Business Card Design Project

Corvexa logo will be provided after
Front

Ned Marrowick- Construction Manager

Ph: (61) 07 53182079
nmarrowick@corvexa-example.com.au
PO Box 83 Kelvorin 4619

Back
Corvexa
EPCM

Oil - Gas - Mining

Industry/Entity Type

Business

Font styles to use
Sans Serif

Colors
faa54b

Requirements
Must have
• White Back Ground

```html
<!DOCTYPE html>
<html lang="en">
<head>
<meta charset="utf-8">
<title>Corvexa Business Cards</title>
<link rel="stylesheet" href="https://fonts.googleapis.com/css2?family=Source+Sans+3:wght@400;600;700&display=swap">
<style>
  :root {
    --stage: #000000;
    --card-white: #f7f7f7;
    --brand-orange: #f5921e;
    --ink: #111111;
    --on-orange: #ffffff;
    --radius: 30px;
  }
  * { margin: 0; padding: 0; box-sizing: border-box; }
  html, body {
    width: 1000px;
    height: 1200px;
    overflow: hidden;
    background: var(--stage);
    font-family: "Source Sans 3", Arial, sans-serif;
  }
  .canvas {
    position: relative;
    width: 1000px;
    height: 1200px;
    background: var(--stage);
  }
  .card {
    position: absolute;
    left: 216px;
    width: 567px;
    height: 327px;
    border-radius: var(--radius);
    overflow: hidden;
  }
  .card--front { top: 80px; background: var(--card-white); }
  .card--back-white { top: 433px; background: var(--card-white); }
  .card--back-orange { top: 793px; background: var(--brand-orange); }

  .card__wave {
    position: absolute;
    inset: 0;
    width: 567px;
    height: 327px;
  }
  .wave__fill { fill: var(--brand-orange); }
  .wave__stroke { fill: var(--ink); }

  .wordmark {
    position: absolute;
    left: 0;
    right: 0;
    text-align: center;
    font-weight: 700;
    font-size: 56px;
    letter-spacing: 10px;
    padding-left: 10px;
    line-height: 1;
    color: var(--ink);
  }
  .card--front .wordmark { top: 70px; }
  .card--back-white .wordmark,
  .card--back-orange .wordmark { top: 144px; }
  .card--back-orange .wordmark { color: var(--on-orange); }

  .person {
    position: absolute;
    left: 37px;
    top: 247px;
    color: var(--on-orange);
  }
  .person__name {
    font-size: 21px;
    font-weight: 600;
    letter-spacing: 0.6px;
    line-height: 1.1;
  }
  .person__role {
    font-size: 16px;
    font-weight: 400;
    padding-left: 10px;
    line-height: 1.3;
  }
  .contact {
    position: absolute;
    right: 18px;
    top: 223px;
    text-align: right;
    color: var(--on-orange);
    font-size: 16.5px;
    line-height: 22.7px;
    font-style: normal;
  }
</style>
</head>
<body>
<main class="canvas">

  <section class="card card--front" aria-label="Business card front">
    <svg class="card__wave" viewBox="0 0 567 327" aria-hidden="true">
      <path class="wave__fill" d="M0 190 C120 232 380 240 567 138 L567 327 L0 327 Z"/>
      <path class="wave__stroke" d="M0 175 C120 215 380 225 567 65 L567 88 C380 236 120 226 0 186 Z"/>
    </svg>
    <div class="wordmark">CORVEXA</div>
    <div class="person">
      <p class="person__name">NED MARROWICK</p>
      <p class="person__role">Construction Manager</p>
    </div>
    <address class="contact">
      PO Box 83<br>
      Kelvorin 4619<br>
      Ph: (61) 07 53182079<br>
      nmarrowick@corvexa-example.com.au
    </address>
  </section>

  <section class="card card--back-white" aria-label="Business card back, white">
    <div class="wordmark">CORVEXA</div>
  </section>

  <section class="card card--back-orange" aria-label="Business card back, orange">
    <div class="wordmark">CORVEXA</div>
  </section>

</main>
</body>
</html>
```